Skyreach e-Sport News site (skyreach.example).

The website will focus on news, results, fixtures, events, team news, upcoming events, team rankings etc. for the Tundrafox FPS game Skyreach (www.playskyreach.example). Site should have the same feel that has been already created by Tundrafox in the official site, with the blues and yellow hues and very graphical. Lots of content needed before the fold, similar sites include www.plexarion.example, www.na.quorbitleague.example, www.vantoplay.example, www.esports.drelvarion.example.

Target Market(s)

Gamers, males, 14-24.

Industry/Entity Type

Events

Font styles to use
Sans Serif
Other font styles liked:
• Big Noodle Titling for large headers.

Requirements
Must have
• A design closely resembling the theme already created by Tundrafox on their official site with use of in-game screenshots and vibrant colours through out.
• Focus on match results, fixtures and team rankings
Nice to have
• Ideal for full width grid layout

```html
<!DOCTYPE html>
<html lang="en">
<head>
<meta charset="utf-8">
<title>Skyreach e-Sport News</title>
<link href="https://fonts.googleapis.com/css2?family=Oswald:wght@500;600&family=Open+Sans:wght@400;600;700&display=swap" rel="stylesheet">
<style>
:root{
  --navy:#0d2650;
  --navy-deep:#081a38;
  --ink:#1f2a36;
  --panel:#eef1f5;
  --rule:#d9dee5;
  --yellow:#f6c21b;
  --text:#3a4350;
  --muted:#7d8693;
  --white:#ffffff;
  --link:#1c2f4d;
}
*{box-sizing:border-box;margin:0;padding:0}
html,body{width:696px;height:1200px;overflow:hidden}
body{
  font-family:"Open Sans",Arial,sans-serif;
  color:var(--text);
  background:radial-gradient(ellipse at 50% 30%,#1a4a86 0%,#0f3062 45%,#081b3c 100%);
  position:relative;
}
.page{position:absolute;left:90px;top:0;width:520px}
.site-header{height:48px;display:flex;align-items:center;justify-content:space-between}
.brand{font-family:"Oswald",sans-serif;font-weight:600;font-size:17px;color:var(--white);letter-spacing:.5px}
.header-tools{display:flex;align-items:center;gap:5px;font-size:6px;color:#c7d3e6}
.social{display:flex;gap:3px}
.social span{width:9px;height:9px;border-radius:50%;background:#e04a3a;display:block}
.social span:nth-child(2){background:#3b8fd8}
.social span:nth-child(3){background:#2b5fa8}
.social span:nth-child(4){background:#d23b3b}
.btn-sm{background:var(--white);color:var(--ink);font-size:6px;padding:2px 5px;border-radius:2px;margin-left:3px}
.main-nav{height:24px;background:var(--white);display:flex;align-items:stretch;font-size:6.5px;font-weight:600;color:var(--ink)}
.main-nav a{display:flex;align-items:center;padding:0 11px;color:inherit;text-decoration:none}
.main-nav a.active{background:var(--yellow)}
.content{background:var(--white);padding:12px 0 10px 0;display:flex;gap:11px;height:814px}
.primary{width:349px;padding-left:3px}
.sidebar{width:157px}
.hero{height:216px;position:relative;background:linear-gradient(135deg,#10204a 0%,#2c56b8 40%,#3aa7d8 60%,#1a2a5c 100%)}
.hero-caption{position:absolute;left:0;right:0;bottom:0;height:30px;background:rgba(8,20,45,.75);padding:5px 8px;color:var(--white)}
.hero-caption h2{font-family:"Oswald",sans-serif;font-size:8.5px;font-weight:500;letter-spacing:.3px}
.hero-caption p{font-size:5px;color:#b8c4d6;margin-top:2px}
.hero-arrows{position:absolute;right:6px;bottom:10px;display:flex;gap:2px}
.hero-arrows span,.pager span{width:10px;height:10px;background:#fff;display:flex;align-items:center;justify-content:center}
.section-head{display:flex;align-items:center;margin:14px 0 9px;height:12px}
.tag{background:var(--yellow);font-family:"Oswald",sans-serif;font-size:6.5px;font-weight:500;color:var(--ink);padding:2px 8px;letter-spacing:.5px}
.section-head .line{flex:1;height:1px;background:var(--rule)}
.pager{display:flex;gap:2px;margin-left:6px}
.pager span{border:1px solid var(--rule)}
.cards{display:grid;gap:9px}
.cards.three{grid-template-columns:repeat(3,1fr)}
.cards.two{grid-template-columns:repeat(2,1fr)}
.card .thumb{height:64px;background:linear-gradient(135deg,#16306a,#3e7fd0 55%,#122650)}
.cards.two .card .thumb{height:66px}
.card .thumb.warm{background:linear-gradient(135deg,#2a1a4a,#6d4bb8 50%,#2a6bc8)}
.card .thumb.teal{background:linear-gradient(135deg,#0e2c44,#2c8cb0 55%,#173a60)}
.card h3{font-size:6px;font-weight:700;color:var(--ink);margin-top:6px;line-height:1.3}
.card p{font-size:5px;color:var(--muted);line-height:1.45;margin-top:3px}
.card .more{display:block;font-size:5px;font-weight:700;color:var(--link);margin-top:5px}
.panel-head{background:var(--ink);color:var(--white);font-family:"Oswald",sans-serif;font-size:6.5px;font-weight:500;letter-spacing:.4px;height:15px;display:flex;align-items:center;justify-content:space-between;padding:0 6px}
.panel-head small{font-family:"Open Sans",sans-serif;font-size:4.5px;color:#aeb8c6}
.panel{background:var(--panel);margin-bottom:16px}
.rank-row{display:flex;align-items:center;gap:4px;height:17px;padding:0 6px;font-size:5px;border-bottom:1px solid var(--rule)}
.rank-row .num{width:6px;color:var(--muted)}
.flag{width:9px;height:6px;background:linear-gradient(#2f5fb8 33%,#fff 33% 66%,#c83a3a 66%)}
.rank-row .pts{margin-left:auto;color:var(--muted)}
.fixture{padding:6px 7px;border-bottom:1px solid var(--rule);font-size:5px;height:40px}
.fixture b{display:block;color:var(--ink);font-weight:600;line-height:1.4}
.fixture span{color:var(--muted);display:block;margin-top:2px}
.result{display:flex;align-items:center;gap:3px;height:15px;padding:0 6px;font-size:4.8px;border-bottom:1px solid var(--rule)}
.result .score{margin:0 auto;font-weight:700;color:var(--ink)}
.result .show{color:var(--link);font-weight:600}
.news-item{display:flex;gap:5px;padding:6px 7px;border-bottom:1px solid var(--rule);font-size:5px}
.news-item .n{width:8px;height:8px;background:var(--yellow);font-size:4.5px;display:flex;align-items:center;justify-content:center;flex:none;font-weight:700}
.news-item b{display:block;color:var(--ink);font-weight:600;line-height:1.35}
.news-item span{display:block;color:var(--muted);line-height:1.4;margin-top:2px}
.site-footer{position:absolute;left:0;top:886px;width:696px;height:314px;background:rgba(6,18,42,.55)}
.footer-inner{position:absolute;left:90px;width:520px;top:22px;display:flex;justify-content:space-between}
.link-cols{display:flex;gap:24px}
.link-cols ul{list-style:none;font-size:5px;color:#b9c6da;line-height:2.1}
.newsletter{width:160px}
.newsletter h4{font-family:"Oswald",sans-serif;font-size:7px;font-weight:500;color:var(--white);letter-spacing:.4px}
.newsletter p{font-size:5px;color:#9fb0c8;margin-top:6px;line-height:1.5}
.input{height:16px;background:#fff;margin-top:18px;font-size:5px;color:var(--muted);padding:0 6px;display:flex;align-items:center}
.subscribe{height:18px;background:var(--yellow);margin-top:6px;font-family:"Oswald",sans-serif;font-size:7px;font-weight:500;color:var(--ink);display:flex;align-items:center;justify-content:center;letter-spacing:.5px}
.footer-bottom{position:absolute;left:90px;width:520px;top:272px;display:flex;align-items:center;justify-content:space-between;font-size:5px;color:#9fb0c8;border-top:1px solid rgba(255,255,255,.15);padding-top:10px}
.footer-bottom .follow{display:flex;align-items:center;gap:5px}
</style>
</head>
<body>
<div class="page">
  <header class="site-header">
    <div class="brand">SKYREACH</div>
    <div class="header-tools">
      <span>Follow us on</span>
      <div class="social"><span></span><span></span><span></span><span></span></div>
      <span class="btn-sm">Login</span><span class="btn-sm">Signup</span>
    </div>
  </header>
  <nav class="main-nav">
    <a class="active">Home</a><a>Latest</a><a>Events</a><a>Matches</a><a>Rankings</a><a>Fixtures</a><a>News</a><a>Teams</a><a>Contact</a>
  </nav>
  <div class="content">
    <main class="primary">
      <section class="hero" role="img" aria-label="In-game tournament screenshot with players on stage">
        <div class="hero-caption">
          <h2>LOREM IPSUM IS SIMPLY DUMMY TEXT</h2>
          <p>Lorem ipsum is simply dummy text of the printing and typesetting industry.</p>
        </div>
        <div class="hero-arrows">
          <span><svg width="5" height="5" viewBox="0 0 5 5"><path d="M3.5 .5L1.5 2.5l2 2" stroke="#1f2a36" fill="none"/></svg></span>
          <span><svg width="5" height="5" viewBox="0 0 5 5"><path d="M1.5 .5l2 2-2 2" stroke="#1f2a36" fill="none"/></svg></span>
        </div>
      </section>

      <div class="section-head"><span class="tag">NEWS</span><span class="line"></span>
        <div class="pager"><span><svg width="5" height="5" viewBox="0 0 5 5"><path d="M3.5 .5L1.5 2.5l2 2" stroke="#7d8693" fill="none"/></svg></span><span><svg width="5" height="5" viewBox="0 0 5 5"><path d="M1.5 .5l2 2-2 2" stroke="#7d8693" fill="none"/></svg></span></div></div>
      <div class="cards three">
        <article class="card"><div class="thumb" role="img" aria-label="Players competing at a tournament desk"></div>
          <h3>Lorem Ipsum is simply dummy</h3><p>It is a long established fact that a reader will be distracted by the layout.</p><a class="more">READ MORE ›</a></article>
        <article class="card"><div class="thumb warm" role="img" aria-label="Arena crowd under stage lights"></div>
          <h3>There are many variations</h3><p>Passages of text are available, but most have suffered some alteration.</p><a class="more">READ MORE ›</a></article>
        <article class="card"><div class="thumb teal" role="img" aria-label="Team on stage with screens behind"></div>
          <h3>Sed ut perspiciatis unde</h3><p>Omnis iste natus error sit voluptatem accusantium doloremque laudantium.</p><a class="more">READ MORE ›</a></article>
      </div>

      <div class="section-head"><span class="tag">EVENTS</span><span class="line"></span>
        <div class="pager"><span><svg width="5" height="5" viewBox="0 0 5 5"><path d="M3.5 .5L1.5 2.5l2 2" stroke="#7d8693" fill="none"/></svg></span><span><svg width="5" height="5" viewBox="0 0 5 5"><path d="M1.5 .5l2 2-2 2" stroke="#7d8693" fill="none"/></svg></span></div></div>
      <div class="cards two">
        <article class="card"><div class="thumb warm" role="img" aria-label="Event hall with players at computers"></div>
          <h3>Sed ut perspiciatis unde omnis iste natus error sit</h3><p>Nemo enim ipsam voluptatem quia voluptas sit aspernatur aut odit aut fugit, sed quia consequuntur magni dolores.</p><a class="more">READ MORE ›</a></article>
        <article class="card"><div class="thumb" role="img" aria-label="Stage lit in blue during a final"></div>
          <h3>On the other hand, we denounce with righteous</h3><p>Indignation and dislike men who are so beguiled by the charms of pleasure of the moment.</p><a class="more">READ MORE ›</a></article>
      </div>

      <div class="section-head"><span class="tag">UPCOMING EVENTS</span><span class="line"></span>
        <div class="pager"><span><svg width="5" height="5" viewBox="0 0 5 5"><path d="M3.5 .5L1.5 2.5l2 2" stroke="#7d8693" fill="none"/></svg></span><span><svg width="5" height="5" viewBox="0 0 5 5"><path d="M1.5 .5l2 2-2 2" stroke="#7d8693" fill="none"/></svg></span></div></div>
      <div class="cards three">
        <article class="card"><div class="thumb teal" role="img" aria-label="Players at gaming stations"></div>
          <h3>Lorem Ipsum is simply dummy</h3><p>It is a long established fact that a reader will be distracted by the layout.</p><a class="more">READ MORE ›</a></article>
        <article class="card"><div class="thumb" role="img" aria-label="Audience watching a match"></div>
          <h3>There are many variations</h3><p>Passages of text are available, but most have suffered some alteration.</p><a class="more">READ MORE ›</a></article>
        <article class="card"><div class="thumb warm" role="img" aria-label="Tournament stage with big screen"></div>
          <h3>Sed ut perspiciatis unde</h3><p>Omnis iste natus error sit voluptatem accusantium doloremque laudantium.</p><a class="more">READ MORE ›</a></article>
      </div>
    </main>

    <aside class="sidebar">
      <section class="panel">
        <div class="panel-head">TEAM RANKING <small>VIEW ALL</small></div>
        <div class="rank-row"><span class="num">1</span><i class="flag"></i>Frostbyte Gaming<span class="pts">1240</span></div>
        <div class="rank-row"><span class="num">2</span><i class="flag"></i>Team Vanta<span class="pts">1198</span></div>
        <div class="rank-row"><span class="num">3</span><i class="flag"></i>Nordlyn Esports<span class="pts">1155</span></div>
        <div class="rank-row"><span class="num">4</span><i class="flag"></i>Kestrel Five<span class="pts">1102</span></div>
        <div class="rank-row"><span class="num">5</span><i class="flag"></i>Hollow Point<span class="pts">1087</span></div>
        <div class="rank-row"><span class="num">6</span><i class="flag"></i>Cinder Club<span class="pts">1040</span></div>
        <div class="rank-row"><span class="num">7</span><i class="flag"></i>Arcline<span class="pts">1012</span></div>
        <div class="rank-row"><span class="num">8</span><i class="flag"></i>Team Solace<span class="pts">996</span></div>
        <div class="rank-row"><span class="num">9</span><i class="flag"></i>Redwake<span class="pts">971</span></div>
        <div class="rank-row"><span class="num">10</span><i class="flag"></i>Quill Raiders<span class="pts">950</span></div>
      </section>
      <section class="panel">
        <div class="panel-head">FIXTURES <small>VIEW ALL</small></div>
        <div class="fixture"><b>Qualifier 1 - Team 1 and Team 2 at Australia</b><span>Sep 26, 2016 - 8:00 pm</span></div>
        <div class="fixture"><b>Qualifier 2 - Team 1 and Team 2 at Australia</b><span>Sep 28, 2016 - 6:00 pm</span></div>
        <div class="fixture"><b>Final 1 - Team 1 and Team 2 at Australia</b><span>Oct 02, 2016 - 7:30 pm</span></div>
        <div class="fixture"><b>Final 2 - Team 1 and Team 2 at Australia</b><span>Oct 04, 2016 - 7:30 pm</span></div>
      </section>
      <section class="panel">
        <div class="panel-head">RESULTS <small>VIEW ALL</small></div>
        <div class="result"><i class="flag"></i>Team 1<span class="score">3 - 1</span>Team 2<i class="flag"></i><span class="show">Show</span></div>
        <div class="result"><i class="flag"></i>Team 3<span class="score">2 - 2</span>Team 4<i class="flag"></i><span class="show">Show</span></div>
        <div class="result"><i class="flag"></i>Team 5<span class="score">0 - 3</span>Team 6<i class="flag"></i><span class="show">Show</span></div>
        <div class="result"><i class="flag"></i>Team 7<span class="score">3 - 2</span>Team 8<i class="flag"></i><span class="show">Show</span></div>
        <div class="result"><i class="flag"></i>Team 1<span class="score">1 - 3</span>Team 5<i class="flag"></i><span class="show">Show</span></div>
        <div class="result"><i class="flag"></i>Team 2<span class="score">3 - 0</span>Team 6<i class="flag"></i><span class="show">Show</span></div>
        <div class="result"><i class="flag"></i>Team 3<span class="score">2 - 3</span>Team 7<i class="flag"></i><span class="show">Show</span></div>
        <div class="result"><i class="flag"></i>Team 4<span class="score">3 - 1</span>Team 8<i class="flag"></i><span class="show">Show</span></div>
        <div class="result"><i class="flag"></i>Team 6<span class="score">0 - 2</span>Team 1<i class="flag"></i><span class="show">Show</span></div>
      </section>
      <section class="panel">
        <div class="panel-head">TEAM NEWS</div>
        <div class="news-item"><span class="n">1</span><div><b>At vero eos et accusamus et iusto odio dignissimos ducimus</b><span>Qui blanditiis praesentium voluptatum deleniti.</span></div></div>
        <div class="news-item"><span class="n">2</span><div><b>On the other hand, we denounce with righteous indignation</b><span>And dislike men who are so beguiled by the charms.</span></div></div>
        <div class="news-item"><span class="n">3</span><div><b>But I must explain to you how all this mistaken idea of denouncing</b><span>Pleasure and praising pain was born.</span></div></div>
      </section>
    </aside>
  </div>
</div>

<footer class="site-footer">
  <div class="footer-inner">
    <div class="link-cols">
      <ul><li>Latest</li><li>Events</li><li>Matches</li><li>Rankings</li><li>Fixtures</li><li>News</li><li>Teams</li><li>Contact</li></ul>
      <ul><li>Algeria 1</li><li>Algeria 2</li><li>Algeria 3</li><li>Algeria 4</li><li>Algeria 5</li><li>Algeria 6</li><li>Algeria 7</li><li>Algeria 8</li></ul>
      <ul><li>Frostbyte Gaming</li><li>Team Vanta</li><li>Nordlyn Esports</li><li>Kestrel Five</li><li>Hollow Point</li><li>Cinder Club</li><li>Arcline</li><li>Team Solace</li></ul>
      <ul><li>Team Results</li><li>Player Standings</li><li>Upcoming Events</li><li>Match Archive</li><li>Press</li></ul>
    </div>
    <div class="newsletter">
      <h4>NEWSLETTER SUBSCRIBE</h4>
      <p>Get the latest results, fixtures and team news straight to your inbox.</p>
      <div class="input">Enter your email</div>
      <div class="subscribe">SUBSCRIBE</div>
    </div>
  </div>
  <div class="footer-bottom">
    <div class="follow">Follow us on <div class="social"><span></span><span></span><span></span><span></span></div></div>
    <span>Copyright © 2016 skyreach.example. All Rights Reserved.</span>
  </div>
</footer>
</body>
</html>
```